Refresh of Business Card Design

Want to refresh the business card design with the new logo while adhering to style guide as attached. Would like to match feel of website www.durmackvinex.com

```html
<!DOCTYPE html>
<html lang="en">
<head>
<meta charset="utf-8">
<title>Durmack Vinex – Business Card</title>
<link href="https://fonts.googleapis.com/css2?family=Arimo:wght@400;700&display=swap" rel="stylesheet">
<style>
  :root {
    --page-bg: #d9d4cd;
    --card-top: #ece9e4;
    --card-bottom: #ddd8d1;
    --card-edge: #b9b3ab;
    --ink: #2a2a2a;
    --ink-soft: #4a4a4a;
    --accent: #9b2a30;
    --rule: #3a3a3a;
  }
  * { margin: 0; padding: 0; box-sizing: border-box; }
  html, body {
    width: 1170px;
    height: 1200px;
    overflow: hidden;
    background: var(--page-bg);
    font-family: "Arimo", Arial, sans-serif;
  }
  .canvas {
    position: relative;
    width: 1170px;
    height: 1200px;
  }
  .card {
    position: absolute;
    left: 85px;
    top: 315px;
    width: 1000px;
    height: 570px;
    border-radius: 34px;
    border: 1.5px solid var(--card-edge);
    background: linear-gradient(180deg, var(--card-top), var(--card-bottom));
    color: var(--ink);
  }
  .brand {
    position: absolute;
    right: 70px;
    top: 128px;
    display: flex;
    align-items: center;
    gap: 18px;
  }
  .brand-dot {
    width: 58px;
    height: 58px;
    border-radius: 50%;
    background: var(--accent);
  }
  .brand-name {
    font-size: 34px;
    font-weight: 400;
    letter-spacing: 2px;
    text-transform: uppercase;
    color: var(--ink);
  }
  .person {
    position: absolute;
    left: 68px;
    top: 368px;
  }
  .person-name {
    font-size: 38px;
    font-weight: 700;
    line-height: 1;
    color: var(--ink-soft);
  }
  .person-role {
    margin-top: 8px;
    font-size: 24px;
    color: var(--accent);
  }
  .email {
    position: absolute;
    right: 70px;
    top: 412px;
    font-size: 24px;
    color: var(--ink);
  }
  .rule {
    position: absolute;
    left: 68px;
    right: 70px;
    top: 452px;
    height: 1.5px;
    background: var(--rule);
  }
  .contact-list {
    position: absolute;
    left: 68px;
    top: 465px;
    list-style: none;
    font-size: 24px;
    color: var(--ink-soft);
  }
  .contact-list li {
    display: flex;
    align-items: center;
    gap: 12px;
    height: 32px;
  }
  .contact-list svg { width: 22px; height: 22px; fill: var(--accent); }
  .address {
    position: absolute;
    right: 70px;
    top: 465px;
    text-align: right;
    font-style: normal;
    font-size: 24px;
    line-height: 32px;
    color: var(--ink);
  }
</style>
</head>
<body>
<main class="canvas">
  <section class="card">
    <div class="brand">
      <span class="brand-dot"></span>
      <span class="brand-name">Durmack Vinex</span>
    </div>

    <div class="person">
      <p class="person-name">Reid Calloway</p>
      <p class="person-role">Sales</p>
    </div>

    <p class="email">rcalloway@durmackvinex.com</p>

    <div class="rule"></div>

    <ul class="contact-list">
      <li>
        <svg viewBox="0 0 24 24" aria-hidden="true"><path d="M6.6 10.8c1.4 2.8 3.8 5.1 6.6 6.6l2.2-2.2c.3-.3.7-.4 1-.2 1.1.4 2.3.6 3.6.6.6 0 1 .4 1 1V20c0 .6-.4 1-1 1C10.6 21 3 13.4 3 4c0-.6.4-1 1-1h3.5c.6 0 1 .4 1 1 0 1.3.2 2.5.6 3.6.1.3 0 .7-.2 1l-2.3 2.2z"/></svg>
        <span>806.555.0142</span>
      </li>
      <li>
        <svg viewBox="0 0 24 24" aria-hidden="true"><circle cx="12" cy="12" r="10"/><path d="M2 12h20M12 2c3 3 3 17 0 20M12 2c-3 3-3 17 0 20" stroke="#e6e2dc" stroke-width="1.5" fill="none"/></svg>
        <span>www.durmackvinex.com</span>
      </li>
    </ul>

    <address class="address">
      P.O.Box 40218 Lakemont, TX 79502<br>
      72 Harlow Ave Fenwick, Texas 79230
    </address>
  </section>
</main>
</body>
</html>
```